依頼詳細
PCとスマホデザインの両方納品をいただきますが、
まずはデザインイメージが確認しやすいPCページのみの提案をお願いします。
スマホページは当選者に納品時にお願いしたいと思います。
スマホサイズについて、表示は横幅375pxで作成し、
デザインデータは2倍の横幅750pxのカンバスサイズで作成してください。
(Retinaディスプレイに対応するため)
レスポンシブウェブデザインを意識したデザインでお願いします。

■サイトマップ
添付の画面遷移図をご確認ください。

■参考サイト
http://www.kurumito.or.jp/

■内容について
以下のサイトのリニューアルになります。
https://e-sorana.jp/

■素材写真
画像データについては、フリー素材から流用して
イメージ画像に当て込んでください。
足りない場合は、一旦他のサイトの写真をサンプルとして
入れてください。(サンプルなどの表記をお願いします)
また、購入が必要な写真などを利用した場合、
価格とサイト名を教えてください。

また、Pixmoor Bankで定期契約をしていますので、
Pixmoor Bankの画像は使用できます。
デザイン時はカンプ画像をお入れいただきますようお願いします。

■ワイヤーフレーム
https://view.plotmesa.com/share/83f41a07-c2e9-4d1b-bb72-5e0a9f7d26c3-4a17/?fullscreen
コンテンツの構成としてワイヤーフレームを作成しましたが
必ずしもワイヤーフレームの通りではなくて大丈夫です。
TOPページに配置するコンテンツを見ていただき、デザインは
デザイナーの皆様におまかせしたいと思います。

----------------------------------------------------------------------------
【制作物に対するお願い】

■フォントについて
・無料で使えるフォントで作成をお願いします。
・OSに紐づくフォントの使用は控えていただければと思います (ヒラギノなど)

■その他
色味やデザインの雰囲気は添付のパンフレットを参考にしてください。
添付のパンフレットの色味
上記のいずれか1つ(アウトラインありとなしの2つ)と高解像度JPGを納品お願いします。
adobe XDでの納品も可能です。

クライアントのイメージ通りでした。

たくさんのご提案ありがとうございました。
次回もぜひ、よろしくお願い致します。

```html
<!DOCTYPE html>
<html lang="ja">
<head>
<meta charset="utf-8">
<title>みどり野市 ひだまり育成会</title>
<link href="https://fonts.googleapis.com/css2?family=Noto+Sans+JP:wght@400;500;700&family=Zen+Maru+Gothic:wght@500;700&display=swap" rel="stylesheet">
<style>
:root{
  --green:#5fae2e;
  --green-dark:#3f7d1c;
  --green-light:#dcedb0;
  --lime:#c8e27a;
  --yellow-soft:#fdf6d6;
  --orange:#f39a1b;
  --text:#333;
  --muted:#666;
  --footer:#8aa54f;
  --white:#fff;
}
*{box-sizing:border-box;margin:0;padding:0}
html,body{width:1200px;height:2600px;overflow:hidden}
body{position:relative;background:var(--white);color:var(--text);font-family:"Noto Sans JP",sans-serif}
.abs{position:absolute}
.round{font-family:"Zen Maru Gothic",sans-serif}

/* header */
.site-header{left:0;top:0;width:1200px;height:60px;z-index:5}
.brand{left:226px;top:18px;color:var(--green-dark)}
.brand small{display:block;font-size:10px;font-weight:500}
.brand strong{font-size:15px;font-weight:700}
.global-nav{left:548px;top:20px;display:flex;gap:22px;font-size:11px;font-weight:500}
.nav-contact{left:820px;top:12px;width:152px;height:32px;border-radius:16px;background:var(--orange);color:#fff;font-size:11px;font-weight:700;display:flex;align-items:center;justify-content:center;gap:6px}

/* hero */
.hero-bg{left:0;top:0;width:1200px;height:720px;background:radial-gradient(ellipse at 15% 35%,#b7d75e 0,#d6e98e 35%,#f1f6c9 60%,#fff 80%)}
.hero-photo{left:460px;top:40px;width:740px;height:632px;border-radius:0 0 0 90px;background:linear-gradient(135deg,#dfe6ec,#b9c6d2 45%,#6d8aa6 75%,#c9d4dc)}
.hero-copy{left:228px;top:278px;color:#fff;font-size:36px;font-weight:700;line-height:1.55;letter-spacing:.06em;text-shadow:0 2px 6px rgba(80,120,20,.35)}

/* section headings */
.sec-icon{width:44px;height:44px;border-radius:50%;background:var(--lime);display:flex;align-items:center;justify-content:center}
.sec-title{width:1200px;left:0;text-align:center;font-size:20px;font-weight:700;color:var(--text);line-height:1.4}

.btn{height:32px;border-radius:16px;background:var(--green);color:#fff;font-size:11px;font-weight:700;display:flex;align-items:center;justify-content:center;gap:8px}
.body-text{font-size:11px;line-height:1.9;color:var(--muted)}

/* about */
.about-blob{left:200px;top:840px;width:420px;height:280px;border-radius:50%;background:radial-gradient(ellipse,#d2ea8f 0,#eef6cf 60%,transparent 72%)}
.about-photo{left:220px;top:860px;width:370px;height:236px;border-radius:40px 10px 40px 10px;background:linear-gradient(135deg,#f4d9b4,#e8c48e 40%,#9fc267 80%)}
.about-head{left:640px;top:918px;font-size:24px;font-weight:700;line-height:1.6}
.about-text{left:640px;top:1006px;width:360px}

/* business */
.biz-bg{left:0;top:1190px;width:1200px;height:430px;background:linear-gradient(180deg,#fff 0,#f1f8dc 40%,#eaf5cc 100%)}
.biz-head{left:220px;top:1316px;font-size:24px;font-weight:700;line-height:1.6}
.biz-text{left:220px;top:1408px;width:360px}
.biz-photo{left:600px;top:1288px;width:380px;height:272px;border-radius:10px 40px 10px 40px;background:linear-gradient(135deg,#f0f3f1,#d3dfe4 45%,#f2c9c7 75%,#e6eee8)}

/* news */
.news-bg{left:0;top:1660px;width:1200px;height:440px;background:var(--yellow-soft)}
.news-list{left:328px;top:1832px;width:544px;list-style:none}
.news-list li{height:38px;margin-bottom:22px;background:#fff;border-radius:8px;display:flex;align-items:center;gap:20px;padding:0 20px;font-size:11px}
.news-list time{color:var(--green-dark);font-weight:500}

/* contact */
.contact-name{left:0;width:1200px;top:2212px;text-align:center;color:var(--green-dark)}
.contact-name small{display:block;font-size:12px;font-weight:500}
.contact-name strong{font-size:22px;font-weight:700}
.tel{left:332px;top:2282px;display:flex;align-items:center;gap:6px;font-size:30px;font-weight:700;color:var(--green-dark);font-family:"Zen Maru Gothic",sans-serif}
.tel-note{left:336px;top:2328px;font-size:10px;color:var(--muted)}
.contact-btn{left:620px;top:2286px;width:360px;height:52px;border-radius:26px;background:var(--orange);color:#fff;font-size:15px;font-weight:700;display:flex;align-items:center;justify-content:center;gap:10px}

/* footer */
.site-footer{left:0;top:2432px;width:1200px;height:168px;background:var(--footer);color:#fff}
.foot-links{position:absolute;top:36px;list-style:none;font-size:10px;line-height:2}
.badge{position:absolute;top:40px;width:70px;height:46px;background:#f4f7ec;border-radius:4px}
.copyright{position:absolute;bottom:14px;left:0;width:1200px;text-align:center;font-size:9px}
</style>
</head>
<body>

<!-- hero -->
<div class="abs hero-bg"></div>
<div class="abs hero-photo" role="img" aria-label="車いすの男性と女性スタッフがオフィスでパソコンを見ながら笑顔で話す写真"></div>
<h1 class="abs hero-copy round">地域の中で<br>自分らしくいきいきと</h1>

<header class="abs site-header">
  <div class="abs brand"><small>社会福祉法人</small><strong>みどり野市 ひだまり育成会</strong></div>
  <nav class="abs global-nav"><span>ひだまり育成会について</span><span>事業内容</span><span>お知らせ</span></nav>
  <a class="abs nav-contact">
    <svg width="12" height="10" viewBox="0 0 12 10"><rect x=".5" y=".5" width="11" height="9" rx="1" fill="none" stroke="#fff"/><path d="M1 1l5 4 5-4" fill="none" stroke="#fff"/></svg>お問い合わせ</a>
</header>

<!-- about -->
<div class="abs sec-icon" style="left:578px;top:758px"><svg width="20" height="20" viewBox="0 0 20 20"><circle cx="10" cy="10" r="6" fill="#fff"/></svg></div>
<h2 class="abs sec-title round" style="top:806px">ひだまり育成会について</h2>
<div class="abs about-blob"></div>
<div class="abs about-photo" role="img" aria-label="エプロン姿のスタッフと利用者が一緒に作業をする写真"></div>
<h3 class="abs about-head round">障がい者のあたりまえを<br>社会のあたりまえに。</h3>
<p class="abs body-text about-text">ひだまり育成会は、障がいのある人とその家族が、地域の中で安心して暮らせる社会をめざして活動しています。<br>誰もが自分らしく生きられるよう、日々の支援と交流の場づくりに取り組んでいます。</p>
<a class="abs btn" style="left:712px;top:1120px;width:188px">ひだまり育成会について <span>›</span></a>

<!-- business -->
<div class="abs biz-bg"></div>
<div class="abs sec-icon" style="left:578px;top:1200px"><svg width="20" height="20" viewBox="0 0 20 20"><circle cx="10" cy="10" r="6" fill="#fff"/></svg></div>
<h2 class="abs sec-title round" style="top:1248px">事業内容</h2>
<h3 class="abs biz-head round">一人ひとりの個性・意志を<br>尊重し、サポートします</h3>
<p class="abs body-text biz-text">通所での作業支援や生活介護、相談支援など、利用者さま一人ひとりに合わせた多様なサービスを提供しています。<br>ご本人の思いを大切にしながら、地域で安心して暮らせるよう寄り添ってまいります。</p>
<a class="abs btn" style="left:300px;top:1556px;width:180px">事業内容を見る <span>›</span></a>
<div class="abs biz-photo" role="img" aria-label="車いすの高齢男性と笑顔で寄り添う女性スタッフの写真"></div>

<!-- news -->
<div class="abs news-bg"></div>
<div class="abs sec-icon" style="left:578px;top:1726px"><svg width="20" height="20" viewBox="0 0 20 20"><circle cx="10" cy="10" r="6" fill="#fff"/></svg></div>
<h2 class="abs sec-title round" style="top:1774px">お知らせ</h2>
<ul class="abs news-list">
  <li><time>2022.00.00</time><span>お知らせタイトルが入ります</span></li>
  <li><time>2022.00.00</time><span>お知らせタイトルが入ります</span></li>
  <li><time>2022.00.00</time><span>お知らせタイトルが入ります</span></li>
</ul>
<a class="abs btn" style="left:506px;top:2010px;width:188px">お知らせ一覧 <span>›</span></a>

<!-- contact -->
<svg class="abs" style="left:0;top:2100px" width="1200" height="332" viewBox="0 0 1200 332">
  <ellipse cx="60" cy="60" rx="260" ry="150" fill="#eef6d4"/>
  <ellipse cx="1150" cy="280" rx="260" ry="130" fill="#eef6d4"/>
</svg>
<div class="abs contact-name"><small>社会福祉法人</small><strong class="round">みどり野市 ひだまり育成会</strong></div>
<div class="abs tel">
  <svg width="26" height="26" viewBox="0 0 24 24"><path d="M6.6 10.8a15 15 0 006.6 6.6l2.2-2.2a1 1 0 011-.25 11.4 11.4 0 003.6.57 1 1 0 011 1V20a1 1 0 01-1 1A17 17 0 013 4a1 1 0 011-1h3.5a1 1 0 011 1c0 1.25.2 2.45.57 3.6a1 1 0 01-.25 1z" fill="#3f7d1c"/></svg>
  0248-31-5870
</div>
<p class="abs tel-note">受付時間：月〜金 9:00〜17:00（土日祝を除く）</p>
<a class="abs contact-btn">
  <svg width="18" height="14" viewBox="0 0 12 10"><rect x=".5" y=".5" width="11" height="9" rx="1" fill="none" stroke="#fff"/><path d="M1 1l5 4 5-4" fill="none" stroke="#fff"/></svg>お問い合わせ</a>

<!-- footer -->
<footer class="abs site-footer">
  <ul class="foot-links" style="left:228px"><li>トップページ</li><li>ひだまり育成会について</li><li>事業内容</li><li>お知らせ</li></ul>
  <ul class="foot-links" style="left:420px"><li>お問い合わせ</li><li>プライバシーポリシー</li><li>サイトマップ</li></ul>
  <div class="badge" style="left:820px"></div>
  <div class="badge" style="left:904px"></div>
  <p class="copyright">Copyright © Hidamari Ikuseikai. All Rights Reserved.</p>
</footer>

</body>
</html>
```